Redesigning Web Pages

I need to redesign a section on my website:
http://kelmor.tv-brosk.com/en/pinecresthall
The complete (Pinecrest Hall) section needs to be redesigned.
The works involves designing only. I have my own development team. You would need to provide me with the designing (psd) files at the end of the project.
Please go through the whole section so that you can see the pages that needs to be redesigned (Note: you can create a demo account to see the inner pages, its ok as this link is on the development server). Again, to be clear, I need only to redesign this section (including its sub pages, like registration, user profile page, etc), not the whole website. Of course, the main page to be designed would be the section "main page" the other inner pages are to match the design of the main section page.
All features, functions, and facilities provided on the section are to remain the same.
The design needs to match the current website format. Keep in mind the look and feel information I have provided for this section. Note: Please view the highlighted area in the attached file. This is the area that needs to be redesigned.
The design would be selected based on the creativity of the designer and understanding of what needs to be done.

```html
<!DOCTYPE html>
<html lang="en">
<head>
<meta charset="utf-8">
<title>Kelmor – Pinecrest Hall</title>
<link href="https://fonts.googleapis.com/css2?family=Arimo:wght@400;700&display=swap" rel="stylesheet">
<style>
:root{
  --green:#8cb42a;
  --green-light:#a9cb3c;
  --green-dark:#6e9419;
  --lime-top:#9cc130;
  --ribbon:#d9c522;
  --ribbon-dark:#b8a40f;
  --slate:#3c3c40;
  --slate-blue:#4a5577;
  --ink:#333;
  --muted:#666;
  --line:#d6d6d6;
  --footer:#3a3a3d;
  --footer-bottom:#2a2a2c;
  --orange-btn:#f2a81c;
  --link-brown:#8a5a12;
}
*{box-sizing:border-box;margin:0;padding:0}
html,body{width:791px;height:1200px;overflow:hidden}
body{position:relative;background:#fff;font-family:"Arimo",Arial,sans-serif;color:var(--ink);font-size:11px}
.abs{position:absolute}

/* header */
.header{left:0;top:0;width:791px;height:140px;background:linear-gradient(180deg,#b5d24a 0%,var(--lime-top) 60%,#8fb526 100%)}
.brand{left:40px;top:36px;display:flex;align-items:center;gap:10px}
.brand-mark{width:36px;height:36px;border-radius:50%;background:#f0b429}
.brand-name{font-size:34px;font-weight:700;color:#3b5a0c;letter-spacing:1px}
.top-tabs{left:293px;top:0;display:flex;gap:8px}
.top-tabs span{display:block;width:84px;height:20px;background:linear-gradient(#fff,#e4e4e4);border-radius:0 0 8px 8px;text-align:center;line-height:20px;font-weight:700;font-size:11px;color:#444}
.languages{left:571px;top:31px;font-weight:700;color:#fff;font-size:11.5px}
.lang-btn{top:31px;width:49px;height:16px;background:var(--orange-btn);border:1px solid #fff3;border-radius:3px;color:#fff;font-size:9px;text-align:center;line-height:15px}
.search{left:574px;top:76px;width:200px;height:31px;background:var(--orange-btn);border-radius:5px;padding:5px}
.search-field{width:158px;height:21px;background:#fff;border-radius:3px;color:#999;font-size:10px;padding:5px 8px}
.search svg{position:absolute;right:9px;top:6px}
.nav{left:0;top:111px;width:791px;height:29px;background:linear-gradient(#86ad25,#749a1a);display:flex;align-items:center;padding-left:6px}
.nav a{color:#fff;text-decoration:none;font-size:11.5px;padding:0 7px;border-left:1px solid #c7dd8a;line-height:14px}
.nav a.home{border-left:none;padding:0 8px 0 2px}

/* cards */
.card{border:1px solid #ccc;border-radius:4px;background:#fff;box-shadow:0 1px 3px #0002}
.tab-dark{background:var(--slate);color:#fff;font-weight:700;font-size:10px;height:24px;line-height:24px;padding-left:14px;clip-path:polygon(0 0,90% 0,100% 100%,0 100%)}
.tab-green{background:var(--green);color:#fff;font-weight:700;font-size:10px;height:24px;line-height:24px;text-align:center;clip-path:polygon(12% 0,100% 0,100% 100%,0 100%)}
.tab-slate{background:var(--slate-blue);color:#fff;font-weight:700;font-style:italic;font-size:11px;height:24px;line-height:24px;text-align:center;clip-path:polygon(14% 0,100% 0,100% 100%,0 100%)}
.section-title{background:linear-gradient(#4e5566,#363b47);color:#fff;font-size:13px;height:26px;line-height:26px;padding-left:14px;clip-path:polygon(0 0,100% 0,95% 100%,0 100%)}

/* polaroids */
.polaroid{width:198px;height:150px}
.polaroid .sheet{position:absolute;inset:0;background:#fff;border:1px solid #ccc;box-shadow:0 1px 3px #0002}
.polaroid .s1{transform:rotate(-4deg)}
.polaroid .s2{transform:rotate(3deg)}
.polaroid .photo{position:absolute;left:24px;top:20px;width:150px;height:86px}
.photo.land{background:linear-gradient(180deg,#c9d6e0 0%,#9fb5a4 25%,#5d8a3c 50%,#3e6a2a 75%,#6e8f4a 100%)}
.photo.flowers{background:linear-gradient(180deg,#8a95a8 0%,#f29a1e 30%,#f07b10 60%,#e8a020 100%)}
.polaroid .cap{position:absolute;left:28px;top:116px;width:150px;font-size:9.5px;font-weight:700}
.cap .t{color:var(--link-brown)}
.cap .s{margin-left:28px;color:#2d3e66}
.cap .u{color:#2d3e66}
.cap .u.red{color:#d23c0a}

/* login */
.login-tab{background:linear-gradient(#a6c93a,#86ac22);color:#fff;font-weight:700;font-size:11px;height:24px;line-height:24px;padding-left:22px;clip-path:polygon(0 0,100% 0,88% 100%,0 100%)}
.field-label{font-size:10px;color:#333}
.field{width:124px;height:17px;border:1px solid #ccc;background:linear-gradient(#eee,#fafafa)}
.btn-submit{width:62px;height:17px;background:linear-gradient(#9ccb2c,#6ea315);border-radius:9px;color:#fff;font-size:10px;text-align:center;line-height:17px}

/* ribbons */
.ribbon{height:23px;line-height:23px;background:linear-gradient(#e6d334,var(--ribbon));color:#fff;font-weight:700;font-size:10.5px;padding-left:14px;clip-path:polygon(0 0,100% 0,96% 50%,100% 100%,0 100%)}
.ribbon b{color:#4a3a06}
.article-title{font-size:11.5px;color:#2d3e66;padding-bottom:5px;border-bottom:1px solid var(--line);width:176px}
.article-text{font-size:9.5px;color:#666;line-height:12px;width:178px;margin-top:5px}

/* reviews */
.reviews-title{left:16px;top:580px;font-size:19px;color:#2a3a5a}
.reviews-title span{color:var(--green)}
.rtab{top:614px;height:25px;line-height:25px;text-align:center;font-size:11px;font-weight:700;border-radius:4px 4px 0 0}
.rtab.on{background:#fff;border:1px solid #ccc;border-bottom:none;color:#333;z-index:2;height:26px}
.rtab.off{background:linear-gradient(#9ec637,#78a01c);color:#fff}
.review-text{left:32px;top:660px;width:716px;font-size:10px;line-height:17px;color:#444}

/* lists */
.list{list-style:none}
.list li{height:20.5px;font-size:11px;color:#333;display:flex;align-items:center;gap:12px}
.list svg{flex:none}

/* footer */
.footer-nav{left:0;top:997px;width:791px;height:25px;background:var(--green);display:flex;justify-content:center;align-items:center}
.footer-nav a{color:#fff;text-decoration:none;font-size:11px;padding:0 11px;border-left:1px solid #d4e6a0;line-height:12px}
.footer-nav a:first-child{border-left:none}
.footer{left:0;top:1022px;width:791px;height:155px;background:var(--footer)}
.fcol h4{color:#fff;font-size:11.5px;font-weight:700;margin-bottom:10px}
.fcol p{color:#e5e5e5;font-size:9.5px;line-height:20.7px}
.fdiv{top:1042px;width:1px;height:115px;background:#555}
.footer-bottom{left:0;top:1177px;width:791px;height:23px;background:var(--footer-bottom);color:#ddd;font-size:9px;text-align:right;padding-right:57px;line-height:23px}
</style>
</head>
<body>

<!-- header -->
<div class="abs header"></div>
<div class="abs brand"><span class="brand-mark"></span><span class="brand-name">KELMOR.com</span></div>
<div class="abs top-tabs"><span>Register</span><span>Login</span></div>
<div class="abs languages">Languages</div>
<div class="abs lang-btn" style="left:645px">English</div>
<div class="abs lang-btn" style="left:698px">Arabic</div>
<div class="abs search">
  <div class="search-field">Search</div>
  <svg width="20" height="20" viewBox="0 0 20 20"><circle cx="8" cy="8" r="6" fill="none" stroke="#fff" stroke-width="2.5"/><line x1="12.5" y1="12.5" x2="18" y2="18" stroke="#fff" stroke-width="3" stroke-linecap="round"/></svg>
</div>
<nav class="abs nav">
  <a class="home" href="#"><svg width="18" height="16" viewBox="0 0 18 16"><path d="M9 1 L1 8 H3.5 V15 H7.5 V10.5 H10.5 V15 H14.5 V8 H17 Z" fill="#fff"/></svg></a>
  <a href="#">Destinations</a><a href="#">Things to do</a><a href="#">Hotels</a><a href="#">Weather</a><a href="#">Maps</a><a href="#">Tours</a><a href="#">Travel Photos</a><a href="#">Travel Articles</a><a href="#">Currency Converter</a><a href="#">Pinecrest Hall</a><a href="#">Contact</a>
</nav>

<!-- travel stories -->
<div class="abs card" style="left:8px;top:147px;width:554px;height:411px"></div>
<div class="abs section-title" style="left:9px;top:148px;width:268px">Share Your Travel Stories and Photos</div>

<div class="abs polaroid" style="left:49px;top:200px"><div class="sheet s1"></div><div class="sheet s2"></div><div class="sheet"></div>
  <div class="photo land" role="img" aria-label="Green hills and a lake"></div>
  <div class="cap"><span class="t">TEST</span><span class="s">Source : </span><span class="u">ravi</span></div></div>
<div class="abs polaroid" style="left:304px;top:200px"><div class="sheet s1"></div><div class="sheet s2"></div><div class="sheet"></div>
  <div class="photo land" role="img" aria-label="Green hills and a lake"></div>
  <div class="cap"><span class="t">TEST</span><span class="s">Source : </span><span class="u">ravi</span></div></div>
<div class="abs polaroid" style="left:49px;top:373px"><div class="sheet s1"></div><div class="sheet s2"></div><div class="sheet"></div>
  <div class="photo flowers" role="img" aria-label="Field of orange flowers"></div>
  <div class="cap"><span class="t">TEST</span><span class="s">Source : </span><span class="u red">tvlark</span></div></div>
<div class="abs polaroid" style="left:304px;top:373px"><div class="sheet s1"></div><div class="sheet s2"></div><div class="sheet"></div>
  <div class="photo flowers" role="img" aria-label="Field of orange flowers"></div>
  <div class="cap"><span class="t">TEST</span><span class="s">Source : </span><span class="u red">tvlark</span></div></div>

<div class="abs tab-dark" style="left:9px;top:533px;width:166px">Submit Your Travel Photos</div>
<div class="abs tab-green" style="left:472px;top:533px;width:89px">View All</div>

<!-- login -->
<div class="abs card" style="left:582px;top:147px;width:197px;height:174px"></div>
<div class="abs login-tab" style="left:583px;top:151px;width:124px">LOGIN</div>
<div class="abs field-label" style="left:595px;top:196px">Username &nbsp;:</div>
<div class="abs field" style="left:647px;top:194px"></div>
<div class="abs field-label" style="left:595px;top:223px">Password &nbsp;&nbsp;:</div>
<div class="abs field" style="left:647px;top:221px"></div>
<div class="abs btn-submit" style="left:653px;top:253px">Submit</div>
<div class="abs" style="left:653px;top:281px;font-size:9.5px;color:#2d3e66;text-decoration:underline">Forgot Password</div>
<div class="abs" style="left:715px;top:300px;font-size:9.5px;color:#333">Register...</div>

<!-- articles -->
<div class="abs card" style="left:582px;top:347px;width:197px;height:213px"></div>
<div class="abs ribbon" style="left:579px;top:359px;width:165px">Latest <b>ARTICLES</b></div>
<div class="abs" style="left:594px;top:390px">
  <div class="article-title">Lorem</div>
  <div class="article-text">Lorem ipsum dolor sit consectetur ing elit. Ut eget turpis mi. Aliquam auctor, lacus vel adipiscing adipiscing, nunc est</div>
</div>
<div class="abs" style="left:594px;top:463px">
  <div class="article-title">Lorem</div>
  <div class="article-text">Lorem ipsum dolor sit consectetur ing elit. Ut eget turpis mi. Aliquam auctor, lacus vel adipiscing adipiscing, nunc</div>
</div>
<div class="abs tab-dark" style="left:583px;top:536px;width:104px;font-size:9.5px;padding-left:8px">Submit Your Story</div>
<div class="abs" style="left:716px;top:543px;font-size:9.5px;font-weight:700;color:#333">View More...</div>

<!-- reviews -->
<div class="abs reviews-title">Latest <span>Reviews</span></div>
<div class="abs card" style="left:9px;top:638px;width:770px;height:124px"></div>
<div class="abs rtab on" style="left:9px;width:140px">THINGS TO DO</div>
<div class="abs rtab off" style="left:160px;width:101px">TOURS</div>
<div class="abs rtab off" style="left:273px;width:103px">HOTELS</div>
<p class="abs review-text">Lorem ipsum dolor sit consectetur ing elit. ut eget turpis mi. Aliquam auctor, lacus vel adipiscing adipiscing, nuncLorem ipsum dolor sit consectetur ing elit. ut eget turpis mi. Aliquam auctor, lacus vel adipiscing adipiscing, nuncLorem ipsum dolor sit consectetur ing elit. ut eget turpis mi. Aliquam auctor, lacus vel adipiscing adipiscing, nuncLorem ipsum dolor sit consectetur ing elit. ut eget turpis mi. Aliquam auctor, lacus vel adipiscing adipiscing, nuncLorem ipsum dolor sit consectetur ing elit. ut eget turpis mi. Aliquam auctor, lacus vel adipiscing adipiscing, nuncLorem ipsum dolor sit consectetur ing elit.</p>
<div class="abs tab-dark" style="left:10px;top:737px;width:166px;padding-left:28px">Submit Your Reviews</div>
<div class="abs tab-green" style="left:690px;top:737px;width:88px">View All</div>

<!-- member / article boxes -->
<div class="abs card" style="left:9px;top:787px;width:178px;height:181px"></div>
<div class="abs ribbon" style="left:6px;top:800px;width:166px">Recent Registered Users</div>
<ul class="abs list" style="left:27px;top:834px">
  <li><svg width="12" height="9" viewBox="0 0 12 9"><rect x="0.5" y="0.5" width="7" height="8" fill="none" stroke="#8cb42a"/><path d="M4 4.5h7M8.5 2l2.5 2.5-2.5 2.5" stroke="#8cb42a" fill="none"/></svg>Webdesigner</li>
  <li><svg width="12" height="9" viewBox="0 0 12 9"><rect x="0.5" y="0.5" width="7" height="8" fill="none" stroke="#8cb42a"/><path d="M4 4.5h7M8.5 2l2.5 2.5-2.5 2.5" stroke="#8cb42a" fill="none"/></svg>Owen Pratt</li>
  <li><svg width="12" height="9" viewBox="0 0 12 9"><rect x="0.5" y="0.5" width="7" height="8" fill="none" stroke="#8cb42a"/><path d="M4 4.5h7M8.5 2l2.5 2.5-2.5 2.5" stroke="#8cb42a" fill="none"/></svg>Karan Mehta</li>
  <li><svg width="12" height="9" viewBox="0 0 12 9"><rect x="0.5" y="0.5" width="7" height="8" fill="none" stroke="#8cb42a"/><path d="M4 4.5h7M8.5 2l2.5 2.5-2.5 2.5" stroke="#8cb42a" fill="none"/></svg>Ravi Anand</li>
  <li><svg width="12" height="9" viewBox="0 0 12 9"><rect x="0.5" y="0.5" width="7" height="8" fill="none" stroke="#8cb42a"/><path d="M4 4.5h7M8.5 2l2.5 2.5-2.5 2.5" stroke="#8cb42a" fill="none"/></svg>Ravi Anand</li>
</ul>
<div class="abs tab-dark" style="left:10px;top:943px;width:162px;font-weight:400;font-size:10.5px;padding-left:11px">View Complete Members List</div>

<div class="abs card" style="left:204px;top:787px;width:179px;height:181px"></div>
<div class="abs ribbon" style="left:202px;top:800px;width:164px">Most Active Users (5)</div>
<ul class="abs list" style="left:222px;top:834px">
  <li><svg width="12" height="9" viewBox="0 0 12 9"><rect x="0.5" y="0.5" width="7" height="8" fill="none" stroke="#8cb42a"/><path d="M4 4.5h7M8.5 2l2.5 2.5-2.5 2.5" stroke="#8cb42a" fill="none"/></svg>Ravi Anand</li>
  <li><svg width="12" height="9" viewBox="0 0 12 9"><rect x="0.5" y="0.5" width="7" height="8" fill="none" stroke="#8cb42a"/><path d="M4 4.5h7M8.5 2l2.5 2.5-2.5 2.5" stroke="#8cb42a" fill="none"/></svg>Nikhil Bose</li>
  <li><svg width="12" height="9" viewBox="0 0 12 9"><rect x="0.5" y="0.5" width="7" height="8" fill="none" stroke="#8cb42a"/><path d="M4 4.5h7M8.5 2l2.5 2.5-2.5 2.5" stroke="#8cb42a" fill="none"/></svg>Ravi Anand</li>
  <li><svg width="12" height="9" viewBox="0 0 12 9"><rect x="0.5" y="0.5" width="7" height="8" fill="none" stroke="#8cb42a"/><path d="M4 4.5h7M8.5 2l2.5 2.5-2.5 2.5" stroke="#8cb42a" fill="none"/></svg>Ravi Anand</li>
  <li><svg width="12" height="9" viewBox="0 0 12 9"><rect x="0.5" y="0.5" width="7" height="8" fill="none" stroke="#8cb42a"/><path d="M4 4.5h7M8.5 2l2.5 2.5-2.5 2.5" stroke="#8cb42a" fill="none"/></svg>Ravi Anand</li>
</ul>
<div class="abs tab-dark" style="left:205px;top:943px;width:162px;font-weight:400;font-size:10.5px;padding-left:11px">View Complete Members List</div>

<div class="abs card" style="left:400px;top:787px;width:179px;height:181px"></div>
<div class="abs ribbon" style="left:400px;top:800px;width:164px;background:linear-gradient(#9ec637,#78a01c)">Most Viewed Article (2)</div>
<ul class="abs list" style="left:418px;top:834px">
  <li><svg width="12" height="9" viewBox="0 0 12 9"><rect x="0.5" y="0.5" width="7" height="8" fill="none" stroke="#8cb42a"/><path d="M4 4.5h7M8.5 2l2.5 2.5-2.5 2.5" stroke="#8cb42a" fill="none"/></svg>Teat</li>
  <li><svg width="12" height="9" viewBox="0 0 12 9"><rect x="0.5" y="0.5" width="7" height="8" fill="none" stroke="#8cb42a"/><path d="M4 4.5h7M8.5 2l2.5 2.5-2.5 2.5" stroke="#8cb42a" fill="none"/></svg>Testing</li>
  <li><svg width="12" height="9" viewBox="0 0 12 9"><rect x="0.5" y="0.5" width="7" height="8" fill="none" stroke="#8cb42a"/><path d="M4 4.5h7M8.5 2l2.5 2.5-2.5 2.5" stroke="#8cb42a" fill="none"/></svg>Teat</li>
  <li><svg width="12" height="9" viewBox="0 0 12 9"><rect x="0.5" y="0.5" width="7" height="8" fill="none" stroke="#8cb42a"/><path d="M4 4.5h7M8.5 2l2.5 2.5-2.5 2.5" stroke="#8cb42a" fill="none"/></svg>Testing</li>
  <li><svg width="12" height="9" viewBox="0 0 12 9"><rect x="0.5" y="0.5" width="7" height="8" fill="none" stroke="#8cb42a"/><path d="M4 4.5h7M8.5 2l2.5 2.5-2.5 2.5" stroke="#8cb42a" fill="none"/></svg>Teat</li>
</ul>
<div class="abs tab-slate" style="left:483px;top:943px;width:95px">Read More...</div>

<div class="abs card" style="left:599px;top:787px;width:177px;height:181px"></div>
<div class="abs ribbon" style="left:599px;top:800px;width:164px;background:linear-gradient(#9ec637,#78a01c);font-size:9.5px">Most Article with Comments (1)</div>
<div class="abs" style="left:618px;top:845px;font-size:11px;color:#333">Testing Ravi</div>
<div class="abs" style="left:620px;top:863px;font-size:11px;color:var(--green)">Comments &nbsp;(1)</div>
<div class="abs tab-slate" style="left:680px;top:943px;width:95px">Read More...</div>

<!-- footer -->
<nav class="abs footer-nav">
  <a href="#">Home</a><a href="#">About</a><a href="#">Hotels</a><a href="#">Weather</a><a href="#">Maps</a><a href="#">Currency Converter</a><a href="#">Contact</a><a href="#">Privacy Policy</a><a href="#">About Our Ads</a><a href="#">Terms of Service</a>
</nav>
<div class="abs footer"></div>
<div class="abs fcol" style="left:71px;top:1041px;width:160px">
  <h4>POPULAR COUNTRIES</h4>
  <p>Australia , Austria , England ,<br>France , Germany , Japan , Kenya<br>, Malaysia , Maldives , Switzerland<br>, Tanzania , Turkey , United Arab<br>Emirates ,</p>
</div>
<div class="abs fdiv" style="left:257px"></div>
<div class="abs fcol" style="left:319px;top:1041px;width:160px">
  <h4>POPULAR CITIES</h4>
  <p>Athens , Athens , Athens , Athens ,<br>Athens , Athens , Athens , Athens ,<br>Athens , Athens , Athens , Athens ,<br>Athens , Athens , Athens , Athens ,<br>Athens , Athens ,</p>
</div>
<div class="abs fdiv" style="left:501px"></div>
<div class="abs fcol" style="left:540px;top:1041px;width:160px">
  <h4>TOP WORLD HOTELS</h4>
  <p>Athens , Athens , Athens , Athens ,<br>Athens , Athens , Athens , Athens ,<br>Athens , Athens , Athens , Athens ,<br>Athens , Athens , Athens , Athens ,<br>Athens , Athens ,</p>
</div>
<div class="abs footer-bottom">© 2012 Kelmor Inc. All rights reserved.</div>

</body>
</html>
```